Letterhead/Envelope/Business Card/Other Stationary
The Velmorant Group
Professional
Tobin Velmorant
President
4718 South Corvell Avenue
Niles, IL 60592
Tobin.Velmorant@velmorantgroup.example
Please do not use any initials like "TVG". Use the attached logo. Also, besides the business card, I would like to see designs for Letterhead, Envelope, Fax Cover and Email Signature.
I am open to it. However, should be modern, corporate and professional.
Franchises
I have attached a white logo on transparent background
I am also attaching dark blue font text for putting on a white background

```html
<!DOCTYPE html>
<html lang="en">
<head>
<meta charset="utf-8">
<title>The Velmorant Group — Stationery Concepts</title>
<link rel="stylesheet" href="https://fonts.googleapis.com/css2?family=Cormorant+Garamond:wght@500&family=Lato:wght@400;700&display=swap">
<style>
  :root {
    --backdrop: #4b3627;
    --paper: #ffffff;
    --paper-shade: #eef0f4;
    --brand-blue: #4a6396;
    --brand-blue-dark: #3a5283;
    --ink: #2f3f63;
    --ink-soft: #7a86a0;
    --label: #d9cbbd;
    --faint: #e6e9ef;
  }
  * { box-sizing: border-box; margin: 0; padding: 0; }
  html, body { width: 1200px; height: 466px; overflow: hidden; }
  body {
    position: relative;
    background: var(--backdrop);
    font-family: "Lato", Arial, sans-serif;
    color: var(--ink);
  }
  .label {
    position: absolute;
    font-size: 5px;
    letter-spacing: 1px;
    text-transform: uppercase;
    color: var(--label);
    text-align: center;
  }
  .wordmark {
    display: flex;
    align-items: center;
    gap: 4px;
    font-family: "Cormorant Garamond", Georgia, serif;
    font-weight: 500;
    color: var(--ink);
    white-space: nowrap;
  }
  .wordmark .mark {
    border: 1px solid var(--ink);
    flex: none;
  }
  .sheet {
    position: absolute;
    background: var(--paper);
    overflow: hidden;
    box-shadow: 0 2px 6px rgba(0,0,0,.35);
  }
  .sheet .band { position: absolute; left: 0; bottom: 0; width: 100%; }

  /* business cards */
  .card { width: 72px; height: 42px; }
  .card-front { left: 12px; top: 196px; }
  .card-front .wordmark { position: absolute; left: 5px; top: 5px; font-size: 4.5px; }
  .card-front .wordmark .mark { width: 5px; height: 5px; }
  .card-front .person { position: absolute; left: 5px; top: 15px; font-size: 3.2px; line-height: 1.35; }
  .card-front .person strong { font-size: 3.6px; }
  .card-back { left: 12px; top: 252px; background: var(--brand-blue); }
  .card-back .centre { position: absolute; inset: 0; display: flex; align-items: center; justify-content: center; }
  .card-back .wordmark { color: var(--paper); font-size: 5px; }
  .card-back .wordmark .mark { border-color: var(--paper); width: 6px; height: 6px; }

  /* letterheads */
  .letterhead { top: 12px; width: 336px; height: 428px; }
  .letterhead-one { left: 96px; }
  .letterhead-two { left: 456px; }
  .letterhead .wordmark { position: absolute; left: 22px; top: 20px; font-size: 11px; }
  .letterhead .wordmark .mark { width: 12px; height: 12px; }
  .letterhead-one .contact {
    position: absolute; left: 176px; top: 18px;
    font-size: 4.2px; line-height: 1.5; color: var(--ink-soft);
  }
  .letterhead-two .watermark {
    position: absolute; left: 0; right: 0; top: 150px;
    text-align: center; font-family: "Cormorant Garamond", Georgia, serif;
    font-size: 34px; color: var(--faint); white-space: nowrap;
  }
  .letterhead-two .footer-contact {
    position: absolute; left: 0; right: 0; bottom: 30px;
    text-align: center; font-size: 4.2px; color: var(--ink-soft);
  }

  /* envelopes */
  .envelope { left: 816px; width: 360px; }
  .env-back-blue-a { top: 14px; height: 70px; background: var(--brand-blue); }
  .env-back-blue-b { top: 92px; height: 76px; background: var(--brand-blue); }
  .env-back-white { top: 184px; height: 80px; }
  .env-front { top: 356px; height: 86px; }
  .envelope svg.flap { position: absolute; inset: 0; width: 100%; height: 100%; }
  .envelope .flap-mark {
    position: absolute; left: 50%; width: 8px; height: 8px; margin-left: -4px;
    border: 1px solid var(--paper);
  }
  .env-back-white .flap-mark { border-color: var(--ink); }
  .env-front .wordmark { position: absolute; left: 14px; top: 10px; font-size: 8px; }
  .env-front .wordmark .mark { width: 9px; height: 9px; }
  .env-front .return { position: absolute; left: 27px; top: 22px; font-size: 3.4px; color: var(--ink-soft); line-height: 1.4; }
</style>
</head>
<body>

  <p class="label" style="left:6px; top:184px; width:84px;">Stationary Concepts</p>

  <!-- Business card front -->
  <section class="sheet card card-front" aria-label="Business card front">
    <div class="wordmark"><span class="mark"></span>The Velmorant Group</div>
    <div class="person">
      <strong>Tobin Velmorant</strong><br>President<br>
      4718 South Corvell Avenue<br>Niles, IL 60592<br>
      Tobin.Velmorant@velmorantgroup.example
    </div>
    <svg class="band" viewBox="0 0 72 6" height="6" preserveAspectRatio="none" aria-hidden="true">
      <path d="M0 3 Q36 0 72 3 V6 H0Z" fill="var(--brand-blue)"/>
    </svg>
  </section>
  <p class="label" style="left:12px; top:241px; width:72px;">Business Card Front</p>

  <!-- Business card back -->
  <section class="sheet card card-back" aria-label="Business card back">
    <div class="centre"><div class="wordmark"><span class="mark"></span>The Velmorant Group</div></div>
  </section>
  <p class="label" style="left:12px; top:297px; width:72px;">Business Card Back</p>

  <!-- Letterhead option 1 -->
  <section class="sheet letterhead letterhead-one" aria-label="Letterhead option 1">
    <div class="wordmark"><span class="mark"></span>The Velmorant Group</div>
    <div class="contact">
      4718 South Corvell Avenue<br>
      Niles, IL 60592<br>
      Tobin.Velmorant@velmorantgroup.example<br>
      velmorantgroup.example
    </div>
    <svg class="band" viewBox="0 0 336 22" height="22" preserveAspectRatio="none" aria-hidden="true">
      <path d="M0 8 Q168 -4 336 8 V22 H0Z" fill="var(--paper-shade)"/>
      <path d="M0 12 Q168 2 336 12 V22 H0Z" fill="var(--brand-blue)"/>
    </svg>
  </section>
  <p class="label" style="left:96px; top:448px; width:336px;">Letter Head Option 1</p>

  <!-- Letterhead option 2 -->
  <section class="sheet letterhead letterhead-two" aria-label="Letterhead option 2">
    <div class="wordmark"><span class="mark"></span>The Velmorant Group</div>
    <div class="watermark" aria-hidden="true">The Velmorant Group</div>
    <div class="footer-contact">
      4718 South Corvell Avenue &nbsp;·&nbsp; Niles, IL 60592 &nbsp;·&nbsp; Tobin.Velmorant@velmorantgroup.example &nbsp;·&nbsp; velmorantgroup.example
    </div>
    <svg class="band" viewBox="0 0 336 22" height="22" preserveAspectRatio="none" aria-hidden="true">
      <path d="M0 8 Q168 -4 336 8 V22 H0Z" fill="var(--paper-shade)"/>
      <path d="M0 12 Q168 2 336 12 V22 H0Z" fill="var(--brand-blue)"/>
    </svg>
  </section>
  <p class="label" style="left:456px; top:448px; width:336px;">Letter Head Option 2</p>

  <!-- Envelopes -->
  <section class="sheet envelope env-back-blue-a" aria-label="Envelope back, blue">
    <svg class="flap" viewBox="0 0 360 70" preserveAspectRatio="none" aria-hidden="true">
      <path d="M0 0 L180 38 L360 0" fill="var(--brand-blue-dark)" stroke="rgba(255,255,255,.35)" stroke-width=".6"/>
    </svg>
    <span class="flap-mark" style="top:26px;"></span>
  </section>

  <section class="sheet envelope env-back-blue-b" aria-label="Envelope back, blue">
    <svg class="flap" viewBox="0 0 360 76" preserveAspectRatio="none" aria-hidden="true">
      <path d="M0 0 L180 40 L360 0" fill="var(--brand-blue-dark)" stroke="rgba(255,255,255,.35)" stroke-width=".6"/>
    </svg>
    <span class="flap-mark" style="top:28px;"></span>
  </section>

  <section class="sheet envelope env-back-white" aria-label="Envelope back, white">
    <svg class="flap" viewBox="0 0 360 80" preserveAspectRatio="none" aria-hidden="true">
      <path d="M0 0 L180 42 L360 0" fill="var(--paper-shade)" stroke="#cfd4de" stroke-width=".6"/>
    </svg>
    <span class="flap-mark" style="top:30px;"></span>
  </section>
  <p class="label" style="left:816px; top:272px; width:360px;">Envelope Option 1</p>

  <section class="sheet envelope env-front" aria-label="Envelope front">
    <div class="wordmark"><span class="mark"></span>The Velmorant Group</div>
    <div class="return">4718 South Corvell Avenue<br>Niles, IL 60592</div>
    <svg class="band" viewBox="0 0 360 14" height="14" preserveAspectRatio="none" aria-hidden="true">
      <path d="M0 6 Q180 -2 360 6 V14 H0Z" fill="var(--brand-blue)"/>
    </svg>
  </section>
  <p class="label" style="left:816px; top:448px; width:360px;">Envelope Option 2</p>

</body>
</html>
```